BRAMWELL Underwriting Trade Show Banner Insurance Underwriting

WE need a design for a trade show banner. BRAMWELL Underwriting Inc. is an independently Canadian owned boutique Managing General Agent that brings unequalled value to our three customers:
​Tailored insurance coverage and products for individual insureds​Support and industry knowledge for our broker partners​
Expert underwriting for our insurance carriers. Our website is https://www.bramwellunderwriting.example. We would like to keep the font the same. I've put more instructions in a word document attached. We want it to flow with our fact sheets. I'm also adding our colors for our logo.

```html
<!DOCTYPE html>
<html lang="en">
<head>
<meta charset="utf-8">
<title>BRAMWELL Underwriting – Trade Show Banners</title>
<link href="https://fonts.googleapis.com/css2?family=Poppins:wght@400;600;700&display=swap" rel="stylesheet">
<style>
  :root{
    --navy:#1f2d5c;
    --navy-deep:#17234a;
    --navy-soft:#2c3d73;
    --mist:#8e9ab6;
    --white:#ffffff;
    --page:#eef0f3;
    --photo-light:#e6e9ee;
    --photo-mid:#c9ced8;
  }
  *{box-sizing:border-box;margin:0;padding:0}
  html,body{width:1200px;height:2768px;overflow:hidden}
  body{background:var(--page);font-family:"Poppins",Arial,sans-serif;position:relative}
  .banner-row{position:absolute;top:644px;left:20px;width:1160px;height:1480px;display:flex;gap:20px}
  .banner{width:570px;height:1480px;background:var(--white);position:relative;overflow:hidden;box-shadow:0 2px 10px rgba(0,0,0,.08)}
  .brand{position:absolute;top:0;left:0;width:100%;height:250px;display:flex;align-items:center;justify-content:center;gap:14px}
  .brand-square{width:22px;height:22px;background:var(--navy)}
  .brand-name{font-weight:600;font-size:34px;color:var(--navy);letter-spacing:1px}
  .navy-band{position:absolute;left:0;width:100%;background:var(--navy)}
  .tagline{position:absolute;left:44px;top:60px;font-weight:700;font-size:62px;line-height:1.12;color:var(--white)}
  .tagline .muted{color:var(--mist)}
  .photo{position:absolute;left:0;width:100%}
  .photo-dishes{top:820px;height:500px;background:radial-gradient(ellipse at 50% 55%,var(--photo-mid) 0%,var(--photo-light) 45%,var(--white) 75%)}
  .photo-lab{top:0;left:0;height:100%;background:linear-gradient(120deg,var(--navy) 30%,var(--navy-soft) 70%,var(--navy) 100%)}
  .section-title{position:absolute;left:44px;top:50px;font-weight:700;font-size:60px;line-height:1.1;color:var(--white)}
  .url-pill{position:absolute;left:40px;right:40px;bottom:44px;height:58px;border-radius:29px;background:var(--navy);color:var(--white);font-weight:600;font-size:19px;display:flex;align-items:center;justify-content:center}
  .product-grid{position:absolute;top:620px;left:30px;right:30px;display:grid;grid-template-columns:1fr 1fr;row-gap:44px;column-gap:20px}
  .product{display:flex;flex-direction:column;align-items:center;text-align:center}
  .product svg{width:86px;height:86px}
  .product-name{margin-top:10px;font-weight:700;font-size:27px;line-height:1.12;color:var(--navy)}
</style>
</head>
<body>
<main class="banner-row">

  <section class="banner banner-values">
    <header class="brand"><span class="brand-square"></span><span class="brand-name">BRAMWELL Underwriting</span></header>
    <div class="navy-band" style="top:250px;height:570px">
      <h1 class="tagline"><span class="muted">Customer<br>Focused.</span><br>Expert<br>Knowledge.<br>Integrity.</h1>
    </div>
    <div class="photo photo-dishes" role="img" aria-label="Photo of stacked clear glass petri dishes"></div>
    <div class="url-pill">https://www.bramwellunderwriting.example</div>
  </section>

  <section class="banner banner-products">
    <header class="brand"><span class="brand-square"></span><span class="brand-name">BRAMWELL Underwriting</span></header>
    <div class="navy-band" style="top:250px;height:320px">
      <div class="photo photo-lab" role="img" aria-label="Faded photo of laboratory glassware in navy tones"></div>
      <h2 class="section-title">Our<br>Products</h2>
    </div>

    <div class="product-grid">
      <div class="product">
        <svg viewBox="0 0 86 86" aria-hidden="true"><circle cx="43" cy="43" r="30" fill="none" stroke="var(--navy)" stroke-width="10" stroke-dasharray="10 6"/><circle cx="43" cy="34" r="8" fill="var(--navy)"/><path d="M29 58a14 12 0 0 1 28 0z" fill="var(--navy)"/></svg>
        <span class="product-name">Directors<br>&amp; Officers</span>
      </div>
      <div class="product">
        <svg viewBox="0 0 86 86" aria-hidden="true"><rect x="18" y="30" width="22" height="44" rx="4" fill="var(--navy)"/><rect x="24" y="18" width="10" height="12" fill="var(--navy)"/><rect x="46" y="40" width="24" height="34" rx="4" fill="var(--navy)"/><circle cx="58" cy="28" r="7" fill="var(--navy)"/></svg>
        <span class="product-name">Spas<br>&amp; Salons</span>
      </div>
      <div class="product">
        <svg viewBox="0 0 86 86" aria-hidden="true"><path d="M43 74 14 45a16 16 0 0 1 29-22 16 16 0 0 1 29 22z" fill="var(--navy)"/><path d="M22 46h14l5-10 6 18 5-8h12" fill="none" stroke="var(--white)" stroke-width="4"/></svg>
        <span class="product-name">Healthcare</span>
      </div>
      <div class="product">
        <svg viewBox="0 0 86 86" aria-hidden="true"><rect x="14" y="30" width="26" height="26" fill="var(--navy)"/><rect x="46" y="30" width="26" height="26" fill="var(--navy)"/><rect x="30" y="6" width="26" height="22" fill="var(--navy)"/><rect x="8" y="60" width="70" height="8" fill="var(--navy)"/></svg>
        <span class="product-name">Wholesale</span>
      </div>
      <div class="product">
        <svg viewBox="0 0 86 86" aria-hidden="true"><path d="M34 10h18v4h-4v20l20 34a6 6 0 0 1-5 8H23a6 6 0 0 1-5-8l20-34V14h-4z" fill="var(--navy)"/></svg>
        <span class="product-name">Life Sciences</span>
      </div>
      <div class="product">
        <svg viewBox="0 0 86 86" aria-hidden="true"><rect x="10" y="16" width="66" height="44" rx="4" fill="var(--navy)"/><rect x="34" y="62" width="18" height="8" fill="var(--navy)"/><rect x="24" y="70" width="38" height="5" fill="var(--navy)"/><path d="M37 28v20l16-10z" fill="var(--white)"/></svg>
        <span class="product-name">Media E &amp; O</span>
      </div>
      <div class="product">
        <svg viewBox="0 0 86 86" aria-hidden="true"><path d="M8 76V42l18-12v12l18-12v12l18-12V14h12v62z" fill="var(--navy)"/></svg>
        <span class="product-name">Manufacturing</span>
      </div>
      <div class="product">
        <svg viewBox="0 0 86 86" aria-hidden="true"><rect x="10" y="28" width="66" height="44" rx="6" fill="var(--navy)"/><path d="M32 28v-8h22v8" fill="none" stroke="var(--navy)" stroke-width="6"/><rect x="10" y="44" width="66" height="4" fill="var(--white)"/></svg>
        <span class="product-name">Misc. E &amp; O</span>
      </div>
    </div>

    <div class="url-pill">https://www.bramwellunderwriting.example</div>
  </section>

</main>
</body>
</html>
```